Web Design for Recruitment Agency

We need a new web design for the company who provides professional services in Labor Recruitment and Home Helpers Hire.

The sections to be covered:
1. About us
2. Philosophy
3. Services
- Labor Recruitment
* skilled workers
* unskilled workers
- Home Helpers
4. Search CV
5. Testimonials
5. Contact us

Examples:
http://www.qorvennaue.com
http://tpmubelo.ae

The website should be clean and elegant. It should portray professionalism and attention to details.

It is important to have interactive and easy-to-navigate design with lots of pictures.

We want clients to get the right impression and be able to request a contact in case they have a requirement. We also want clients to be able to search for CVs that are already in the database. CV should be displayed as a profile card (photo and brief information about the candidate).

Logo is attached.

Target Market(s)

Local families, companies.

Industry/Entity Type

It Company

Number of Pages Required

1 page

Font styles to use
Sans Serif

Requirements
Must have
• Clean layout with pictures
Nice to have
• Dynamic, engaging website.

```html
<!DOCTYPE html>
<html lang="en">
<head>
<meta charset="utf-8">
<title>KVR Recruitment</title>
<link rel="stylesheet" href="https://fonts.googleapis.com/css2?family=Questrial&family=Open+Sans:wght@400;600;700&display=swap">
<style>
:root{
  --purple:#2a0f6b;
  --green:#1f8a34;
  --blue:#3a97dc;
  --mint:#48c983;
  --ink:#333;
  --muted:#8a8f99;
  --band:#f2f2f7;
  --card1:#1fb4d8;
  --card2:#4b88c4;
  --card3:#1784a6;
  --card4:#4cc0b6;
  --footer:#3d3f42;
  --quote:#2b8fe0;
}
*{margin:0;padding:0;box-sizing:border-box}
html,body{width:1200px;height:2397px;overflow:hidden;background:#fff}
body{position:relative;font-family:"Open Sans",Arial,sans-serif;color:var(--ink)}
.abs{position:absolute}
.q{font-family:"Questrial","Century Gothic",sans-serif}

/* header */
.logo{left:165px;top:22px;display:flex;align-items:center;gap:8px}
.logo-dot{width:22px;height:22px;border-radius:50%;background:var(--green)}
.logo-name{font-family:"Questrial",sans-serif;font-size:26px;color:var(--purple)}
.call{left:808px;top:19px;font-size:11px;color:#555}
.call b{color:var(--purple);font-size:12px}
.submit-cv{left:943px;top:13px;width:96px;height:26px;background:var(--purple);color:#fff;font-size:11px;display:flex;align-items:center;justify-content:center}
.nav{top:89px;left:462px;width:578px;display:flex;justify-content:space-between;font-size:12.5px;color:#444}

/* hero */
.hero{left:0;top:121px;width:1200px;height:435px;background:linear-gradient(90deg,#4b4b4b 0%,#6a5a46 30%,#3e3e3e 60%,#2a2a2a 100%)}
.hero-title{left:586px;top:296px;font-size:35px;color:#fff}
.hero-text{left:586px;top:345px;width:454px;font-size:12.5px;line-height:14px;color:#fff}
.learn{left:588px;top:419px;width:163px;height:43px;background:var(--green);color:#fff;font-size:14px;display:flex;align-items:center;justify-content:center}
.search{left:161px;top:532px;width:878px;height:53px;background:#fff;box-shadow:0 1px 4px rgba(0,0,0,.15)}
.search-ph{left:30px;top:19px;font-size:10px;color:#aaa}
.search-btn{right:0;top:0;width:139px;height:53px;background:var(--green);color:#fff;font-size:16px;display:flex;align-items:center;justify-content:center}

.section-title{left:0;width:1200px;text-align:center;font-size:28px;color:#222}
.section-sub{left:0;width:1200px;text-align:center;font-size:13.5px;color:var(--muted)}

/* category panels */
.panel{top:748px;width:439px;height:212px;color:#fff;text-align:center}
.panel-blue{left:161px;background:var(--blue)}
.panel-green{left:600px;background:var(--mint)}
.panel-head{position:absolute;top:46px;left:0;width:100%;display:flex;justify-content:center;align-items:center;gap:12px;font-size:25px}
.panel-icon{width:34px;height:34px;border-radius:50%;background:rgba(255,255,255,.25)}
.panel-sub{position:absolute;top:99px;left:0;width:100%;font-size:12px}
.panel-btn{position:absolute;top:134px;left:123px;width:192px;height:34px;border-radius:17px;font-size:12px;display:flex;align-items:center;justify-content:center}
.panel-blue .panel-btn{background:#2a78b5}
.panel-green .panel-btn{background:#3aa96b}

/* services */
.services{left:0;top:1039px;width:1200px;height:399px;background:var(--band)}
.svc{top:1175px;width:178px;height:222px;color:#fff;text-align:center;box-shadow:0 1px 3px rgba(0,0,0,.15)}
.svc-icon{position:absolute;left:47px;top:13px;width:84px;height:84px;border-radius:50%;background:#fff;display:flex;align-items:center;justify-content:center}
.svc-title{position:absolute;top:110px;width:100%;font-size:14px;font-weight:700}
.svc-text{position:absolute;top:139px;left:20px;width:138px;font-size:10px;line-height:13px}
.svc-more{position:absolute;top:182px;left:51px;width:77px;height:19px;background:#fff;color:#555;font-size:10px;display:flex;align-items:center;justify-content:center}

/* about / philosophy */
.info-head{top:1470px;display:flex;align-items:center;gap:16px}
.info-icon{width:30px;height:30px;border-radius:50%;background:#111;color:#fff;font-weight:700;font-size:18px;display:flex;align-items:center;justify-content:center;font-family:Georgia,serif}
.info-title{font-size:21px;color:var(--purple);border-bottom:2px solid var(--purple);padding-bottom:2px}
.info-text{top:1514px;width:360px;font-size:11px;line-height:18.7px;color:#777}
.info-more{top:1640px;width:74px;height:19px;background:var(--purple);color:#fff;font-size:10px;display:flex;align-items:center;justify-content:center}

/* testimonials */
.testi{left:0;top:1723px;width:1200px;height:207px;background:linear-gradient(180deg,#eef3f8,#e4ecf3)}
.testi-title{left:0;top:1748px;width:1200px;text-align:center;font-size:20px;font-weight:700;color:var(--purple)}
.testi-line{top:1762px;height:2px;background:#333}
.avatar{left:236px;top:1788px;width:106px;height:106px;border-radius:50%;border:3px solid var(--purple);background:linear-gradient(180deg,#7a5a48,#c9a58e)}
.quote-mark{font-family:Georgia,serif;font-size:34px;color:var(--quote);font-weight:700}
.testi-text{left:412px;top:1809px;width:540px;font-size:12px;line-height:19px;color:#333}
.testi-by{left:640px;top:1876px;width:314px;text-align:right;font-size:11px;line-height:13px;color:var(--quote)}

/* gallery */
.gallery{left:0;top:1985px;width:1200px;height:262px;background:linear-gradient(180deg,#4aa3dd,#a6cdec);border-radius:4px}
.gallery-title{left:0;top:1996px;width:1200px;text-align:center;font-size:28px;color:#fff}
.photo{top:2060px;width:192px;height:142px;border:1px solid #fff}
.arrow{top:2118px}

/* footer */
.footer{left:0;top:2261px;width:1200px;height:136px;background:var(--footer)}
.foot-link{top:2329px;font-size:11px;color:#c9c9c9}
.copy{left:177px;top:2360px;font-size:10px;color:#aaa}
.foot-contact{left:884px;font-size:11px;color:#bbb}
.social{top:2367px;width:15px;height:15px;border-radius:50%;border:1.5px solid #aaa}
</style>
</head>
<body>

<!-- header -->
<div class="abs logo"><span class="logo-dot"></span><span class="logo-name">KVR</span></div>
<div class="abs call">Call Us <b>+65 6120 4470</b></div>
<div class="abs submit-cv">Submit CV</div>
<nav class="abs nav q">
  <span>About us</span><span>Philosophy</span><span>Services</span><span>Search CV</span><span>Testimonials</span><span>Contact us</span>
</nav>

<!-- hero -->
<div class="abs hero" role="img" aria-label="Smiling construction worker in a yellow hard hat carrying timber boards"></div>
<div class="abs hero-title q">Job Searching Just Got Easy</div>
<div class="abs hero-text">Curabitur et lorem a massa tempus aliquam. Aenean aliquam volutpat gravida. Pellentesque in neque nec tortor sagittis tempor quis in lectus. Vestibulum vehicula aliquet elit ut porta.</div>
<div class="abs learn q">LEARN MORE</div>
<div class="abs search">
  <span class="abs search-ph">Please Enter your key word here...</span>
  <div class="abs search-btn q">Search CV</div>
</div>

<!-- intro -->
<div class="abs section-title q" style="top:640px">Lorem Ipsum is simply dummy text?</div>
<div class="abs section-sub q" style="top:692px">Simply lorem Ipsum is simply dummy text of the printing and typesetting industry. Lorem Ipsum</div>

<div class="abs panel panel-blue">
  <div class="panel-head q"><span class="panel-icon"></span>Labor Recruitment</div>
  <div class="panel-sub">Search or browse for your help Skilled Workers</div>
  <div class="panel-btn">All Skilled Workers</div>
</div>
<div class="abs panel panel-green">
  <div class="panel-head q"><span class="panel-icon"></span>Home Helpers</div>
  <div class="panel-sub">Search or browse for your help Home Helpers</div>
  <div class="panel-btn">All UnSkilled Workers</div>
</div>

<!-- services -->
<div class="abs services"></div>
<div class="abs section-title q" style="top:1066px">Our Services</div>
<div class="abs section-sub q" style="top:1119px">Simply lorem Ipsum is simply dummy text of the printing and typesetting industry. Lorem Ipsum</div>

<div class="abs svc" style="left:192px;background:var(--card1)">
  <div class="svc-icon"><svg width="44" height="44" viewBox="0 0 44 44"><path d="M8 36 L30 14" stroke="var(--card1)" stroke-width="6" stroke-linecap="round"/><path d="M10 10 L34 34" stroke="var(--card1)" stroke-width="5" stroke-linecap="round"/><circle cx="32" cy="12" r="6" fill="none" stroke="var(--card1)" stroke-width="4"/></svg></div>
  <div class="svc-title">Simply lorem text</div>
  <div class="svc-text">Simply lorem Ipsum is simply dummy text</div>
  <div class="svc-more">MORE</div>
</div>
<div class="abs svc" style="left:404px;background:var(--card2)">
  <div class="svc-icon"><svg width="44" height="44" viewBox="0 0 44 44"><circle cx="16" cy="8" r="5" fill="#555"/><rect x="12" y="14" width="8" height="16" rx="2" fill="#555"/><rect x="24" y="22" width="14" height="10" fill="var(--card2)"/><circle cx="27" cy="36" r="3" fill="#555"/><circle cx="36" cy="36" r="3" fill="#555"/></svg></div>
  <div class="svc-title">Dummy text of</div>
  <div class="svc-text">Simply lorem Ipsum is simply dummy text</div>
  <div class="svc-more">MORE</div>
</div>
<div class="abs svc" style="left:618px;background:var(--card3)">
  <div class="svc-icon"><svg width="44" height="44" viewBox="0 0 44 44"><rect x="4" y="20" width="22" height="12" fill="var(--card3)"/><path d="M26 24 H34 L38 29 V32 H26 Z" fill="var(--card3)"/><circle cx="11" cy="34" r="3" fill="#555"/><circle cx="32" cy="34" r="3" fill="#555"/><circle cx="30" cy="12" r="8" fill="none" stroke="var(--card3)" stroke-width="2"/><text x="30" y="15" font-size="8" text-anchor="middle" fill="var(--card3)" font-family="Arial,sans-serif">24</text></svg></div>
  <div class="svc-title">Simply lorem text</div>
  <div class="svc-text">Simply lorem Ipsum is simply dummy text</div>
  <div class="svc-more">MORE</div>
</div>
<div class="abs svc" style="left:833px;background:var(--card4)">
  <div class="svc-icon"><svg width="44" height="44" viewBox="0 0 44 44"><circle cx="18" cy="26" r="9" fill="none" stroke="var(--card4)" stroke-width="6" stroke-dasharray="4 3"/><circle cx="18" cy="26" r="4" fill="var(--card4)"/><circle cx="31" cy="12" r="6" fill="none" stroke="var(--card4)" stroke-width="4" stroke-dasharray="3 2"/></svg></div>
  <div class="svc-title">Dummy text of</div>
  <div class="svc-text">Simply lorem Ipsum is simply dummy text</div>
  <div class="svc-more">MORE</div>
</div>

<!-- about / philosophy -->
<div class="abs info-head" style="left:162px"><span class="info-icon">i</span><span class="info-title q">About us</span></div>
<div class="abs info-text" style="left:162px">Lorem Ipsum is simply dummy text of the printing and typesetting industry. Lorem Ipsum has been the industry's standard dummy text ever since the 1500s, when an unknown printer took a galley of type and scrambled it to make a type specimen book. It has survived not only five centuries, including versions of Lorem Ipsum.</div>
<div class="abs info-more" style="left:441px">MORE</div>

<div class="abs info-head" style="left:681px"><span class="info-icon">&#9775;</span><span class="info-title q">Philosophy</span></div>
<div class="abs info-text" style="left:681px">Lorem Ipsum is simply dummy text of the printing and typesetting industry. Lorem Ipsum has been the industry's standard dummy text ever since the 1500s, when an unknown printer took a galley of type and scrambled it to make a type specimen book. It has survived not only five centuries, including versions of Lorem Ipsum.</div>
<div class="abs info-more" style="left:962px">MORE</div>

<!-- testimonials -->
<div class="abs testi"></div>
<div class="abs testi-line" style="left:180px;width:293px"></div>
<div class="abs testi-line" style="left:725px;width:293px"></div>
<div class="abs testi-title">Testmonials</div>
<div class="abs avatar" role="img" aria-label="Portrait photo of a client"></div>
<span class="abs quote-mark" style="left:378px;top:1795px">&ldquo;</span>
<div class="abs testi-text">Lorem Ipsum is simply dummy text of the printing and typesetting industry. Lorem Ipsum has been the industry's standard dummy text ever since the 1500s, when an unknown printer took a galley of type and scrambled.</div>
<span class="abs quote-mark" style="left:700px;top:1836px">&rdquo;</span>
<div class="abs testi-by">A big weight was lifted off my shoulders<br>( Mara Lindqvist, London )</div>

<!-- gallery -->
<div class="abs gallery"></div>
<div class="abs gallery-title q">Gallary</div>
<svg class="abs arrow" style="left:160px" width="18" height="24" viewBox="0 0 18 24"><path d="M13 3 L4 12 L13 21" stroke="#fff" stroke-width="3" fill="none"/></svg>
<svg class="abs arrow" style="left:1022px" width="18" height="24" viewBox="0 0 18 24"><path d="M5 3 L14 12 L5 21" stroke="#fff" stroke-width="3" fill="none"/></svg>
<div class="abs photo" style="left:203px;background:linear-gradient(180deg,#2d4e72,#8fb2cf)" role="img" aria-label="Worker silhouetted against a large window frame"></div>
<div class="abs photo" style="left:407px;background:linear-gradient(180deg,#f3ede6,#c89a6a)" role="img" aria-label="Couple carrying cardboard moving boxes"></div>
<div class="abs photo" style="left:612px;background:linear-gradient(180deg,#8a6c45,#3e4a5a)" role="img" aria-label="Builder in a yellow hard hat at work"></div>
<div class="abs photo" style="left:817px;background:linear-gradient(180deg,#d9d4cc,#a07850)" role="img" aria-label="Workers in hard hats on a construction site"></div>

<!-- footer -->
<div class="abs footer"></div>
<span class="abs foot-link" style="left:177px">Home</span>
<span class="abs foot-link" style="left:248px">About us</span>
<span class="abs foot-link" style="left:332px">Philosophy</span>
<span class="abs foot-link" style="left:428px">Services</span>
<span class="abs foot-link" style="left:511px">Search CV</span>
<span class="abs foot-link" style="left:604px">Contact us</span>
<div class="abs copy">&copy; 2015 KVR , All Rights Reserved.</div>
<div class="abs foot-contact" style="top:2319px">hello@kvrstaffing.com</div>
<div class="abs foot-contact" style="top:2340px">(902) 418 660 27</div>
<span class="abs social" style="left:884px"></span>
<span class="abs social" style="left:908px"></span>
<span class="abs social" style="left:932px"></span>
<span class="abs social" style="left:956px"></span>

</body>
</html>
```